Wheels for Harborline Website Design

We need a NEW design and uploaded to Hostavero.com. Here is the current site: http://www.wheelsforharborline.org

Need a form like this:

https://brightlanegifts.org/

```html
<!DOCTYPE html>
<html lang="en">
<head>
<meta charset="utf-8">
<title>Wheels for Harborline – Donate a Car</title>
<link href="https://fonts.googleapis.com/css2?family=Work+Sans:ital,wght@0,400;0,500;0,600;0,700;1,400&display=swap" rel="stylesheet">
<style>
:root{
  --navy:#10105a;
  --navy-call:#16167a;
  --red:#e03a3a;
  --ink:#2a2a3a;
  --light:#f6f6f6;
  --white:#fff;
}
*{box-sizing:border-box;margin:0;padding:0}
html,body{width:1200px;height:2411px;overflow:hidden}
body{font-family:"Work Sans",Arial,sans-serif;color:var(--ink);background:var(--white);font-size:13px;line-height:19px;position:relative}
.wrap{position:absolute;left:172px;width:856px}
a{color:inherit;text-decoration:none}

/* top bar */
.topbar{position:absolute;top:0;left:0;width:1200px;height:41px;background:var(--navy);color:#fff;font-size:10.5px}
.topbar .open{position:absolute;left:173px;top:12px}
.topbar .links{position:absolute;left:470px;top:13px;display:flex;gap:62px}
.topbar .call{position:absolute;left:735px;top:0;width:465px;height:41px;background:var(--navy-call);clip-path:polygon(0 0,100% 0,100% 100%,6px 100%)}
.call .ring{position:absolute;left:33px;top:8px;width:26px;height:26px;border-radius:50%;background:#fff;display:flex;align-items:center;justify-content:center}
.call .label{position:absolute;left:68px;top:6px;font-size:10.5px;line-height:12px}
.call .num{position:absolute;left:68px;top:19px;font-size:14px;font-weight:600;line-height:16px}

/* nav */
.nav{position:absolute;top:41px;left:0;width:1200px;height:61px;background:#fff}
.logo{position:absolute;left:172px;top:18px;font-size:19px;font-weight:600;color:var(--navy)}
.menu{position:absolute;left:467px;top:22px;display:flex;gap:31px;font-size:13px;font-weight:500;color:#222}
.btn-donate{position:absolute;left:900px;top:14px;width:128px;height:34px;background:var(--red);color:#fff;font-size:11.5px;font-weight:600;display:flex;align-items:center;justify-content:center;border-radius:2px}

/* hero */
.hero{position:absolute;top:102px;left:0;width:1200px;height:498px}
.hero-photo{position:absolute;inset:0;background:linear-gradient(180deg,#d9e5ef 0%,#e6ebef 45%,#d8dadb 70%,#f4f4f4 100%)}
.hero-swoosh{position:absolute;left:0;top:0}
.form-panel{position:absolute;left:663px;top:0;width:365px;height:444px;background:var(--navy);color:#fff;text-align:center}
.form-panel::before,.form-panel::after{content:"";position:absolute;top:34px;width:3px;height:350px;background:var(--red)}
.form-panel::before{left:-3px}.form-panel::after{right:-3px}
.form-title{margin-top:20px;font-size:16.5px;font-weight:700;letter-spacing:.2px}
.form-divider{margin:10px auto 0;display:flex;align-items:center;justify-content:center;gap:14px}
.form-divider span{display:block;width:104px;height:1px;background:#fff}
.form-sub{margin-top:18px;font-size:14.5px;font-weight:600}
.fields{position:absolute;left:21px;top:116px;width:323px}
.field{height:34px;background:#fff;color:#222;font-size:12px;text-align:left;padding:0 12px;display:flex;align-items:center;justify-content:space-between;margin-bottom:11px}
.row{display:flex;gap:11px}
.row .field{flex:1}
.caret{width:0;height:0;border-left:4px solid transparent;border-right:4px solid transparent;border-top:5px solid #222}
.submit{height:34px;background:var(--red);color:#fff;font-size:11.5px;font-weight:600;display:flex;align-items:center;justify-content:center}

/* features */
.features{top:646px;display:flex}
.feature{width:293px;display:flex;gap:18px}
.feature svg{flex:none;margin-top:12px}
.feature h3{font-size:14.5px;font-weight:600;color:var(--navy);line-height:18px;margin-bottom:5px}
.feature p{font-size:12.5px;line-height:19px;width:190px}

/* why */
.why{position:absolute;top:800px;left:0;width:1200px;height:511px;background:var(--light)}
.why-photo{position:absolute;left:0;top:0;width:517px;height:511px;background:linear-gradient(135deg,#cbcbcb 0%,#d6d3d0 50%,#bdb6b0 100%)}
.why-body{position:absolute;left:588px;top:69px;width:440px}
.h2{font-size:28px;line-height:32px;font-weight:400;color:var(--navy);letter-spacing:.3px}
.h2 b{font-weight:700}
.why-list{margin-top:18px;list-style:none}
.why-list li{display:flex;gap:13px;margin-bottom:11px;font-size:12.5px;line-height:19px}
.why-list li svg{flex:none;margin-top:3px}
.why-list strong{font-weight:600;color:#111}

/* goal */
.goal{top:1384px}
.goal-text{width:418px}
.goal-text p{margin-top:14px;text-align:justify;font-size:12.5px;line-height:19px}
.goal-text p:first-of-type{margin-top:20px}
.goal-frame{position:absolute;left:491px;top:5px;width:365px;height:326px;background:var(--navy);padding:9px}
.goal-photo{width:100%;height:100%;background:linear-gradient(90deg,#8a8f96 0%,#a2a6a8 35%,#7e9a5d 60%,#6f8f48 100%)}

/* who */
.who{position:absolute;top:1790px;left:0;width:1200px;height:315px;background:linear-gradient(180deg,#efefef,#e9e9e9)}
.who-inner{position:absolute;left:172px;top:69px;width:856px;text-align:center}
.who-inner p{margin-top:14px;text-align:left;font-size:12.2px;line-height:19px}
.who-inner blockquote{margin-top:14px;font-style:italic;font-size:13.2px;line-height:19px;color:#333}

/* footer */
.footer{position:absolute;top:2105px;left:0;width:1200px;height:306px;background:var(--navy);color:#fff}
.fcol{position:absolute;top:54px}
.fcol h4{font-size:14.5px;font-weight:600;line-height:18px}
.fcol h4::after{content:"";display:block;width:30px;height:1px;background:var(--red);margin-top:9px}
.fcol ul{list-style:none;margin-top:18px;font-size:12px;line-height:21px}
.fcol p{margin-top:18px;font-size:12px;line-height:19px;width:265px}
.flogo{margin-top:26px;font-size:19px;font-weight:600}
.contact li{display:flex;gap:8px;margin-bottom:12px;line-height:16px}
.contact svg{flex:none;margin-top:3px}
.copy{position:absolute;left:172px;top:263px;width:856px;border-top:1px solid #2c2c78;text-align:center;font-size:11.5px;padding-top:13px}
</style>
</head>
<body>

<header class="topbar">
  <div class="open">We're Open Now</div>
  <div class="links"><a href="#">Location</a><a href="#">Contact Us</a></div>
  <div class="call">
    <div class="ring"><svg width="13" height="13" viewBox="0 0 24 24"><path fill="#10105a" d="M6.6 10.8a15.2 15.2 0 0 0 6.6 6.6l2.2-2.2c.3-.3.7-.4 1-.2 1.1.4 2.3.6 3.6.6.6 0 1 .4 1 1V20c0 .6-.4 1-1 1A17 17 0 0 1 3 4c0-.6.4-1 1-1h3.5c.6 0 1 .4 1 1 0 1.3.2 2.5.6 3.6.1.3 0 .7-.2 1z"/></svg></div>
    <div class="label">Call Us Today To Donate</div>
    <div class="num">800-555-0147</div>
  </div>
</header>

<nav class="nav">
  <div class="logo">Logo Goes Here</div>
  <div class="menu"><a href="#">How To Donate</a><a href="#">Why Donate</a><a href="#">FAQ</a><a href="#">About</a><a href="#">Blog</a></div>
  <a class="btn-donate" href="#">DONATE A CAR</a>
</nav>

<section class="hero">
  <div class="hero-photo" role="img" aria-label="Red sports car with white racing stripes parked in front of a city skyline"></div>
  <svg class="hero-swoosh" width="1200" height="498" viewBox="0 0 1200 498">
    <path d="M0 358 Q330 440 663 424 L663 438 Q330 460 0 380 Z" fill="#e03a3a"/>
    <path d="M1028 384 Q1110 360 1200 352 L1200 430 Q1110 420 1028 420 Z" fill="#e03a3a"/>
  </svg>
  <form class="form-panel">
    <div class="form-title">DONATE YOUR CAR ONLINE 24/7</div>
    <div class="form-divider"><span></span>
      <svg width="30" height="14" viewBox="0 0 30 14"><path d="M2 10V7l4-1 4-4h9l5 4 4 1v3h-2M7 10H2M23 10H11" fill="none" stroke="#e03a3a" stroke-width="1.4"/><circle cx="9" cy="10.5" r="2" fill="none" stroke="#e03a3a" stroke-width="1.4"/><circle cx="21" cy="10.5" r="2" fill="none" stroke="#e03a3a" stroke-width="1.4"/></svg>
      <span></span></div>
    <div class="form-sub">Full Tax Deduction – Running or Not</div>
    <div class="fields">
      <div class="field">First Name</div>
      <div class="field">Last Name</div>
      <div class="field">Phone No</div>
      <div class="field">Email Addres</div>
      <div class="row"><div class="field">Choose Year<span class="caret"></span></div><div class="field">Choose Make<span class="caret"></span></div></div>
      <div class="field">Vehicle Model</div>
      <div class="submit">DONATE MY VEHICLE NOW</div>
    </div>
  </form>
</section>

<section class="wrap features">
  <div class="feature">
    <svg width="56" height="44" viewBox="0 0 56 44" fill="none" stroke="#e03a3a" stroke-width="1.6"><path d="M2 34V22h20V12h12l8 10h10v12H2zM22 22h20M6 4l22 14M2 14l10 8"/><circle cx="12" cy="36" r="4" fill="#fff"/><circle cx="42" cy="36" r="4" fill="#fff"/></svg>
    <div><h3>FAST, FREE PICKUP</h3><p>Lorem ipsum dolor sit amet, consectetur adipiscing elit, sed do eiusmod tempor</p></div>
  </div>
  <div class="feature">
    <svg width="48" height="56" viewBox="0 0 48 56" fill="none" stroke="#e03a3a" stroke-width="1.6"><path d="M16 12h16l-4-9H20zM16 12C6 20 2 30 4 40c2 10 10 14 20 14s18-4 20-14c2-10-2-20-12-28"/><path d="M30 28c-1-3-4-4-6-4-3 0-6 2-6 5 0 6 12 3 12 9 0 3-3 5-6 5-3 0-6-2-6-4M24 20v27"/></svg>
    <div><h3>SAVE MONEY</h3><p>Lorem ipsum dolor sit amet, consectetur adipiscing elit, sed do eiusmod tempor</p></div>
  </div>
  <div class="feature">
    <svg width="54" height="54" viewBox="0 0 54 54" fill="none" stroke="#e03a3a" stroke-width="1.6"><circle cx="27" cy="27" r="25"/><path d="M27 40s-11-7-11-14a6 6 0 0 1 11-3 6 6 0 0 1 11 3c0 7-11 14-11 14z"/></svg>
    <div><h3>YOU HELP KIDS</h3><p>Lorem ipsum dolor sit amet, consectetur adipiscing elit, sed do eiusmod tempor</p></div>
  </div>
</section>

<section class="why">
  <div class="why-photo" role="img" aria-label="Two children peeking around a wall"></div>
  <div class="why-body">
    <h2 class="h2"><b>WHY DONATE YOUR</b> CAR TO US</h2>
    <ul class="why-list">
      <li><svg width="18" height="18" viewBox="0 0 18 18"><circle cx="9" cy="9" r="9" fill="#e03a3a"/><path d="M7 5l4 4-4 4" fill="none" stroke="#fff" stroke-width="1.5"/></svg><span><strong>Lorem ipsum dolor sit amet</strong> : consectetur adipiscing elit, sed do eiusmod tempor incididunt ut labore et dolore magna aliqua. Quis ipsum suspendisse ultrices gravida.</span></li>
      <li><svg width="18" height="18" viewBox="0 0 18 18"><circle cx="9" cy="9" r="9" fill="#e03a3a"/><path d="M7 5l4 4-4 4" fill="none" stroke="#fff" stroke-width="1.5"/></svg><span><strong>Lorem ipsum dolor sit amet</strong> : consectetur adipiscing elit, sed do eiusmod tempor incididunt ut labore et dolore magna aliqua. Quis ipsum suspendisse ultrices gravida.</span></li>
      <li><svg width="18" height="18" viewBox="0 0 18 18"><circle cx="9" cy="9" r="9" fill="#e03a3a"/><path d="M7 5l4 4-4 4" fill="none" stroke="#fff" stroke-width="1.5"/></svg><span><strong>Lorem ipsum dolor sit amet</strong> : consectetur adipiscing elit, sed do eiusmod tempor incididunt ut labore et dolore magna aliqua. Quis ipsum suspendisse ultrices gravida.</span></li>
      <li><svg width="18" height="18" viewBox="0 0 18 18"><circle cx="9" cy="9" r="9" fill="#e03a3a"/><path d="M7 5l4 4-4 4" fill="none" stroke="#fff" stroke-width="1.5"/></svg><span><strong>Lorem ipsum dolor sit amet</strong> : consectetur adipiscing elit, sed do eiusmod tempor incididunt ut labore et dolore magna aliqua. Quis ipsum suspendisse ultrices gravida.</span></li>
      <li><svg width="18" height="18" viewBox="0 0 18 18"><circle cx="9" cy="9" r="9" fill="#e03a3a"/><path d="M7 5l4 4-4 4" fill="none" stroke="#fff" stroke-width="1.5"/></svg><span><strong>Lorem ipsum dolor sit amet</strong> : consectetur adipiscing elit, sed do eiusmod tempor incididunt ut labore et dolore magna aliqua. Quis ipsum suspendisse ultrices gravida.</span></li>
    </ul>
  </div>
</section>

<section class="wrap goal">
  <div class="goal-text">
    <h2 class="h2"><b>HELP US REACH</b> OUR GOAL</h2>
    <p>Lorem ipsum dolor sit amet, consectetur adipiscing elit, sed do eiusmod tempor incididunt ut labore et dolore magna aliqua. Ut enim ad minim veniam, quis nostrud exercitation ullamco laboris nisi ut aliquip ex ea commodo consequat. Duis aute irure dolor in reprehenderit in voluptate velit esse cillum dolore eu fugiat nulla pariatur. Excepteur sint occaecat cupidatat non proident, sunt in culpa qui officia deserunt mollit anim id est laborum.</p>
    <p>Sed ut perspiciatis unde omnis iste natus error sit voluptatem accusantium doloremque laudantium, totam rem aperiam, eaque ipsa quae ab illo inventore veritatis et quasi architecto beatae vitae dicta sunt explicabo. Nemo enim ipsam voluptatem quia voluptas sit aspernatur aut odit aut fugit, sed quia consequuntur magni dolores eos qui ratione voluptatem sequi.</p>
  </div>
  <div class="goal-frame"><div class="goal-photo" role="img" aria-label="Adult and small child walking hand in hand along a path"></div></div>
</section>

<section class="who" role="img" aria-label="Faint photo of a family walking outdoors">
  <div class="who-inner">
    <h2 class="h2"><b>WHO WE</b> ARE</h2>
    <p>Lorem ipsum dolor sit amet, consectetur adipiscing elit, sed do eiusmod tempor incididunt ut labore et dolore magna aliqua. Ut enim ad minim veniam, quis nostrud exercitation ullamco laboris nisi ut aliquip ex ea commodo consequat. Duis aute irure dolor in reprehenderit in voluptate velit esse cillum dolore eu fugiat nulla pariatur. Excepteur sint occaecat cupidatat non proident, sunt in culpa qui officia deserunt mollit anim id</p>
    <blockquote>“Lorem ipsum dolor sit amet, consectetur adipiscing elit, sed do eiusmod tempor incididunt ut labore et dolore magna aliqua. Ut enim ad minim veniam, quis nostrud exercitation ullamco laboris nisi ut aliquip ex ea commodo consequat. Duis aute irure dolor in reprehenderit in voluptate velit esse cillum”</blockquote>
  </div>
</section>

<footer class="footer">
  <div class="fcol" style="left:172px">
    <h4>ABOUT US</h4>
    <p>Lorem ipsum dolor sit amet, consectetur adipiscing elit, sed do eiusmod tempor incididunt ut labore et dolore magna aliqua. Quis ipsum suspendisse ultrices gravida.</p>
    <div class="flogo">Logo Goes Here</div>
  </div>
  <div class="fcol" style="left:509px">
    <h4>NAVIGATION</h4>
    <ul><li>How To Donate</li><li>Why Donate</li><li>Faq</li><li>About Us</li><li>Blog</li><li>Contact Us</li></ul>
  </div>
  <div class="fcol" style="left:665px">
    <h4>RESOURCES</h4>
    <ul><li>Location</li><li>Privacy Policy</li><li>Site Map</li><li>Tax filing info</li><li>Vacation voucher</li><li>Who we help</li></ul>
  </div>
  <div class="fcol" style="left:831px">
    <h4>CONTACT INFO</h4>
    <ul class="contact">
      <li><svg width="10" height="12" viewBox="0 0 10 12"><path d="M5 0a4 4 0 0 0-4 4c0 3 4 8 4 8s4-5 4-8a4 4 0 0 0-4-4zm0 5.5A1.5 1.5 0 1 1 5 2.5a1.5 1.5 0 0 1 0 3z" fill="#e03a3a"/></svg><span>4120 Ferrow Bend Road<br>Calder Springs, TN 37422</span></li>
      <li><svg width="11" height="11" viewBox="0 0 24 24"><path fill="none" stroke="#e03a3a" stroke-width="2.4" d="M6.6 10.8a15.2 15.2 0 0 0 6.6 6.6l2.2-2.2 4.6 1V20A17 17 0 0 1 3 4h4.5l1 4.6z"/></svg><span>800-555-0147</span></li>
      <li><svg width="12" height="9" viewBox="0 0 12 9"><rect width="12" height="9" fill="#e03a3a"/><path d="M0 0l6 5 6-5" fill="none" stroke="#10105a" stroke-width="1"/></svg><span>hello@wheelsforharborline.org</span></li>
    </ul>
  </div>
  <div class="copy">Copyright © 2020 Company Name. All Rights Reserved.</div>
</footer>

</body>
</html>
```